Postcard Mail Out - Wendell

We are a real estate company. We need a post card to mail out to potential clients to try and sale their land. We will attached a couple of post cards that we like but we do not want to copy them completely. We do need to put the Fair Dwelling Access and the Homebroker logos with a disclosure saying not intended to solicit currently listed properties. The image below is what we had started working on. We would like to include something about farm land, timber, maybe a pond, something along those lines. The PDF Files attached are a flyer that was mailed out by another company that we do not want to copy completely. Attached also will be our company's Logo.

Requirements
Must have
• We do need to put the Fair Dwelling Access and the Homebroker logos with a disclosure saying not intended to solicit currently listed properties.<br/><br/>At Cal Moreno Summit Realty, we are blessed to have one of the very best Rural Land Specialists available. Wendell has years of experience promoting and selling rural land properties. Wendell has earned the trust of many landowners, as he is so PASSIONATE in all regards to rural land, farms and ranches. He has made a wide range of landowners very happy throughout his years in Real Estate. Call him today and show him your property, and he will provide you with a free analysis and strategy to maximize the return on your property.
Nice to have
• A picture of Wendell has been added to use on the back of the post card with his phone and number. It would be nice to have a east Texas scenery picture behind him instead of an office.<br/><br/>Please include front and back of post card in your submission.
Should not have
• Should not have Ferris Dunmore's information on the postcard. That post card was just to show what we was wanting. The agent we want listed is Wendell Pruitt and his phone number is (555)413-2086.

```html
<!DOCTYPE html>
<html lang="en">
<head>
<meta charset="utf-8">
<title>Postcard Mail Out – Wendell Pruitt</title>
<link rel="stylesheet" href="https://fonts.googleapis.com/css2?family=Libre+Baskerville:wght@400;700&family=Montserrat:wght@300;400;700;800&family=Ubuntu:wght@400;500&display=swap">
<style>
  :root {
    --canvas: #eef0f2;
    --card-white: #ffffff;
    --ink: #111111;
    --hill-green: #4f5a35;
    --field-green: #5f6a38;
    --silver-light: #f4f4f4;
    --silver-mid: #c9c9c9;
    --silver-dark: #9a9a9a;
    --white-text: #ffffff;
  }
  * { box-sizing: border-box; margin: 0; padding: 0; }
  html, body { width: 1200px; height: 800px; overflow: hidden; }
  body {
    background: var(--canvas);
    display: flex; align-items: center; justify-content: center; gap: 30px;
    font-family: "Ubuntu", sans-serif;
  }
  .postcard {
    position: relative; width: 570px; height: 380px; overflow: hidden;
    background: var(--card-white);
    box-shadow: 0 6px 18px rgba(0,0,0,.18);
  }

  /* ---------- Back side ---------- */
  .back-scenery {
    position: absolute; left: 0; top: 0; width: 340px; height: 380px;
    background: linear-gradient(180deg, #3b4a44 0%, #37452f 35%, var(--hill-green) 55%, var(--field-green) 80%, #525a30 100%);
  }
  .back-intro {
    position: absolute; left: 0; top: 0; width: 340px; height: 175px;
    background: rgba(50,52,48,.72);
    padding: 22px 18px 0 22px;
    color: var(--white-text); font-size: 9.3px; line-height: 1.42;
  }
  .brand {
    position: absolute; left: 30px; top: 192px;
    display: flex; align-items: center; gap: 7px;
    color: var(--white-text); white-space: nowrap;
    font-family: "Libre Baskerville", serif; font-weight: 400; font-size: 11.5px;
  }
  .brand-mark { width: 20px; height: 20px; background: var(--white-text); flex: none; }
  .agent-band {
    position: absolute; left: 0; top: 252px; width: 300px; height: 70px;
    background: linear-gradient(90deg, var(--silver-light), var(--silver-mid) 70%, var(--silver-dark));
    padding: 8px 0 0 26px;
  }
  .agent-name {
    font-family: "Libre Baskerville", serif; font-weight: 700; font-size: 22px; color: var(--ink);
    white-space: nowrap;
  }
  .agent-contact {
    list-style: none; margin-top: 4px;
    font-family: "Montserrat", sans-serif; font-weight: 400; font-size: 12px; color: var(--ink);
    line-height: 1.35;
  }
  .agent-contact li { display: flex; align-items: center; gap: 5px; }
  .agent-contact svg { width: 10px; height: 10px; }
  .agent-portrait {
    position: absolute; left: 262px; top: 128px; width: 108px; height: 252px;
    background: linear-gradient(180deg, #b8b0a8 0%, #1f2430 30%, #1c2230 75%, #2c3448 100%);
    border-radius: 40px 40px 0 0;
  }
  .stamp-box {
    position: absolute; right: 42px; top: 22px; width: 70px; height: 78px;
    border: 1.5px solid var(--ink);
  }

  /* ---------- Front side ---------- */
  .front-art { position: absolute; inset: 0; }
  .headline-banner {
    position: absolute; left: 28px; top: 204px; width: 340px; height: 42px;
    background: linear-gradient(90deg, var(--silver-light), var(--silver-mid) 75%, var(--silver-dark));
    display: flex; align-items: center; justify-content: center;
    white-space: nowrap;
    font-family: "Libre Baskerville", serif; font-weight: 700; font-size: 20px; color: var(--ink);
    letter-spacing: .3px;
  }
  .tagline-bar {
    position: absolute; left: 50px; top: 246px; width: 318px; height: 28px;
    background: var(--ink); color: var(--white-text);
    display: flex; align-items: center; justify-content: center;
    white-space: nowrap;
    font-family: "Montserrat", sans-serif; font-weight: 800; font-size: 14px;
  }
  .compliance-marks {
    position: absolute; right: 24px; top: 256px;
    display: flex; gap: 12px;
  }
  .compliance-mark {
    display: flex; flex-direction: column; align-items: center; gap: 3px;
    font-family: "Montserrat", sans-serif; font-weight: 700; font-size: 5.5px; color: var(--ink);
    text-transform: uppercase; white-space: nowrap;
  }
  .compliance-mark span.shape { width: 26px; height: 26px; background: var(--ink); display: block; }
  .disclaimer-bar {
    position: absolute; right: 0; bottom: 26px; width: 300px; height: 20px;
    background: var(--ink); color: var(--white-text);
    display: flex; align-items: center; justify-content: center;
    white-space: nowrap;
    font-family: "Libre Baskerville", serif; font-size: 9.5px;
  }
</style>
</head>
<body>

  <section class="postcard postcard-back" aria-label="Postcard back">
    <div class="back-scenery" role="img" aria-label="East Texas rolling hills and green pasture scenery"></div>
    <p class="back-intro">
      At Cal Moreno Summit Realty, we are blessed to have one of the very best Rural Land Specialists available. Wendell has years of experience promoting and selling rural land properties. Wendell has earned the trust of many landowners, as he is so PASSIONATE in all regards to rural land, farms and ranches. He has made many landowners very happy. Call him today and show him your property, and he will provide you with a free analysis and strategy to maximize your return on your investment.
    </p>
    <div class="brand"><span class="brand-mark"></span>Cal Moreno Summit Realty</div>
    <div class="agent-band">
      <h2 class="agent-name">Wendell Pruitt</h2>
      <ul class="agent-contact">
        <li>
          <svg viewBox="0 0 10 10" aria-hidden="true"><path d="M2 1 L4 1 L4.6 3 L3.4 3.8 Q4.6 6 6.2 6.6 L7 5.4 L9 6 L9 8 Q5 9 2.4 6 Q0.8 3.6 2 1Z" fill="#111"/></svg>
          (555)413-2086
        </li>
        <li>
          <svg viewBox="0 0 10 10" aria-hidden="true"><circle cx="5" cy="5" r="4.3" fill="none" stroke="#111" stroke-width="1"/><ellipse cx="5" cy="5" rx="1.8" ry="4.3" fill="none" stroke="#111" stroke-width=".8"/><line x1=".7" y1="5" x2="9.3" y2="5" stroke="#111" stroke-width=".8"/></svg>
          summitlandco.com
        </li>
      </ul>
    </div>
    <div class="agent-portrait" role="img" aria-label="Photo of agent Wendell Pruitt on the phone"></div>
    <div class="stamp-box" aria-label="Stamp area"></div>
  </section>

  <section class="postcard postcard-front" aria-label="Postcard front">
    <svg class="front-art" viewBox="0 0 570 380">
      <defs>
        <linearGradient id="bgScene" x1="0" y1="0" x2="0" y2="1">
          <stop offset="0" stop-color="#b9cbdd"/>
          <stop offset=".5" stop-color="#c7d2c2"/>
          <stop offset="1" stop-color="#a9b894"/>
        </linearGradient>
        <linearGradient id="pasture" x1="0" y1="0" x2="0" y2="1">
          <stop offset="0" stop-color="#7aa14a"/>
          <stop offset=".55" stop-color="#5c8a3a"/>
          <stop offset="1" stop-color="#8fa07a"/>
        </linearGradient>
        <linearGradient id="timber" x1="0" y1="0" x2="1" y2="1">
          <stop offset="0" stop-color="#c7d6c8"/>
          <stop offset=".35" stop-color="#7a5a36"/>
          <stop offset=".8" stop-color="#4c6a2c"/>
          <stop offset="1" stop-color="#6f8f3a"/>
        </linearGradient>
        <linearGradient id="pond" x1="0" y1="0" x2="0" y2="1">
          <stop offset="0" stop-color="#7e9a5a"/>
          <stop offset=".35" stop-color="#4f6e8a"/>
          <stop offset=".8" stop-color="#31506e"/>
          <stop offset="1" stop-color="#5e7a48"/>
        </linearGradient>
      </defs>
      <rect width="570" height="380" fill="url(#bgScene)" role="img" aria-label="Sky and wooded valley landscape"/>
      <polygon points="290,30 570,12 570,230 300,232" fill="url(#timber)" stroke="#1a1a1a" stroke-width="5" role="img" aria-label="Tall pine timber forest"/>
      <polygon points="52,78 330,60 388,148 340,212 52,222" fill="url(#pasture)" stroke="#1a1a1a" stroke-width="5" role="img" aria-label="Herd of cattle grazing on green farm land"/>
      <polygon points="8,230 268,226 290,256 268,368 8,372" fill="url(#pond)" stroke="#1a1a1a" stroke-width="5" role="img" aria-label="Pond reflecting trees"/>
    </svg>
    <div class="headline-banner">HAVE LAND FOR SALE?</div>
    <div class="tagline-bar">We Specialize in Rural Land Sales</div>
    <div class="compliance-marks">
      <div class="compliance-mark"><span class="shape"></span>Fair Dwelling Access</div>
      <div class="compliance-mark"><span class="shape"></span>Homebroker</div>
    </div>
    <div class="disclaimer-bar">Not intended to solicit currently listed properties.</div>
  </section>

</body>
</html>
```